Medical Company in need of Modern business card design for new Wound Care clinic.

Modern business card design for our Woundcare company. Logo and description of services can be found on our website; https://www.tovrel-woundcare.com/

```html
<!DOCTYPE html>
<html lang="en">
<head>
<meta charset="utf-8">
<title>Tovrel Woundcare – Business Card</title>
<link rel="stylesheet" href="https://fonts.googleapis.com/css2?family=Montserrat:wght@400;500&family=Tinos:wght@400;700&display=swap">
<style>
  :root {
    --backdrop: #2b241a;
    --card-black: #050505;
    --gold: #c89a4a;
    --gold-light: #f0c766;
    --gold-deep: #b47a2c;
  }
  * { margin: 0; padding: 0; box-sizing: border-box; }
  html, body { width: 1200px; height: 800px; overflow: hidden; }
  body {
    background: var(--backdrop);
    display: flex;
    align-items: center;
    justify-content: center;
    gap: 40px;
  }
  .card {
    position: relative;
    width: 540px;
    height: 309px;
    background: var(--card-black);
    box-shadow: 0 18px 40px rgba(0,0,0,0.55);
    overflow: hidden;
  }
  .wordmark {
    font-family: "Montserrat", Arial, sans-serif;
    font-weight: 400;
    color: var(--gold);
    letter-spacing: 0.22em;
    text-transform: uppercase;
    white-space: nowrap;
    display: flex;
    align-items: center;
    gap: 14px;
  }
  .wordmark-square {
    width: 14px;
    height: 14px;
    background: var(--gold);
  }
  .card-front .wordmark {
    position: absolute;
    left: 50%;
    top: 50%;
    transform: translate(-50%, -50%);
    font-size: 27px;
  }
  .card-back .wordmark {
    position: absolute;
    left: 55%;
    top: 92px;
    transform: translateX(-50%);
    font-size: 21px;
  }
  .holder {
    position: absolute;
    left: 36px;
    top: 172px;
    font-family: "Tinos", "Times New Roman", serif;
    color: var(--gold);
    text-transform: uppercase;
  }
  .holder-name { font-size: 19px; font-weight: 700; letter-spacing: 0.02em; }
  .holder-title { font-size: 11px; font-weight: 400; letter-spacing: 0.04em; margin-top: 1px; }
  .contact-list {
    position: absolute;
    left: 48px;
    top: 218px;
    display: grid;
    grid-template-columns: 150px auto;
    row-gap: 7px;
    column-gap: 24px;
    font-family: "Tinos", "Times New Roman", serif;
    font-weight: 700;
    font-size: 10.5px;
    color: var(--gold);
  }
  .contact-item { display: flex; align-items: center; gap: 8px; white-space: nowrap; }
  .contact-item.wide { grid-column: 1 / span 2; }
  .contact-icon { width: 14px; height: 14px; flex: none; }
  .gold-band {
    position: absolute;
    left: 0;
    bottom: 0;
    width: 100%;
    height: 22px;
  }
</style>
</head>
<body>

  <section class="card card-front" aria-label="Business card front">
    <div class="wordmark"><span class="wordmark-square"></span>Tovrel Woundcare</div>
  </section>

  <section class="card card-back" aria-label="Business card back">
    <div class="wordmark"><span class="wordmark-square"></span>Tovrel Woundcare</div>

    <div class="holder">
      <p class="holder-name">Marcus Hale</p>
      <p class="holder-title">General Director</p>
    </div>

    <div class="contact-list">
      <div class="contact-item">
        <svg class="contact-icon" viewBox="0 0 14 14"><circle cx="7" cy="7" r="6.3" fill="none" stroke="#c89a4a" stroke-width="1"/><path d="M4.6 4.2c.4-.4.9-.3 1.1.1l.5.9c.2.3 0 .6-.2.8-.3.2-.2.6.1 1 .4.5.8.8 1.1.9.3.1.5-.1.7-.3.3-.2.6-.2.8 0l.7.6c.3.3.3.7-.1 1-.6.5-1.5.6-2.6-.1-1.1-.7-2-1.8-2.3-2.8-.2-.8 0-1.6.2-2.1z" fill="#c89a4a"/></svg>
        <span>555-014-2868</span>
      </div>
      <div class="contact-item">
        <svg class="contact-icon" viewBox="0 0 14 14"><circle cx="7" cy="7" r="6.3" fill="none" stroke="#c89a4a" stroke-width="1"/><rect x="3.8" y="5" width="6.4" height="4.2" fill="#c89a4a"/><path d="M3.8 5l3.2 2.4L10.2 5" fill="none" stroke="#050505" stroke-width="0.8"/></svg>
        <span>info@tovrel-woundcare.com</span>
      </div>
      <div class="contact-item">
        <svg class="contact-icon" viewBox="0 0 14 14"><circle cx="7" cy="7" r="6.3" fill="none" stroke="#c89a4a" stroke-width="1"/><rect x="4" y="6" width="6" height="4" fill="#c89a4a"/><rect x="5" y="3.8" width="4" height="2.4" fill="none" stroke="#c89a4a" stroke-width="0.8"/></svg>
        <span>555-014-2867</span>
      </div>
      <div class="contact-item">
        <svg class="contact-icon" viewBox="0 0 14 14"><circle cx="7" cy="7" r="6.3" fill="none" stroke="#c89a4a" stroke-width="1"/><circle cx="7" cy="7" r="3.4" fill="none" stroke="#c89a4a" stroke-width="0.9"/><path d="M3.6 7h6.8M7 3.6c-1.6 2-1.6 4.8 0 6.8M7 3.6c1.6 2 1.6 4.8 0 6.8" fill="none" stroke="#c89a4a" stroke-width="0.7"/></svg>
        <span>www.tovrel-woundcare.com</span>
      </div>
      <div class="contact-item wide">
        <svg class="contact-icon" viewBox="0 0 14 14"><circle cx="7" cy="7" r="6.3" fill="none" stroke="#c89a4a" stroke-width="1"/><path d="M7 10.6L4.9 7.3a2.4 2.4 0 1 1 4.2 0z" fill="#c89a4a"/><circle cx="7" cy="6.1" r="0.9" fill="#050505"/></svg>
        <span>1820 Larkin Ave Ste 200 PMB 41827 Fairview, TX 75069</span>
      </div>
    </div>

    <svg class="gold-band" viewBox="0 0 540 22" preserveAspectRatio="none" aria-hidden="true">
      <defs>
        <linearGradient id="bandGold" x1="0" y1="0" x2="1" y2="0">
          <stop offset="0" stop-color="#b47a2c"/>
          <stop offset="0.45" stop-color="#f0c766"/>
          <stop offset="0.75" stop-color="#d8a446"/>
          <stop offset="1" stop-color="#f0c766"/>
        </linearGradient>
      </defs>
      <rect x="0" y="0" width="540" height="22" fill="url(#bandGold)"/>
      <polygon points="448,0 462,0 470,22 456,22" fill="#050505"/>
      <line x1="442" y1="0" x2="442" y2="22" stroke="#050505" stroke-width="2"/>
    </svg>
  </section>

</body>
</html>
```